Veltrand Nickel

I am putting together a presentation and want to establish a theme. This is one of the core slides. It shows a process of data travelling from left to right to a visual outcome. My design is obviously awful. I need something that looks much more professional and sets the them for the rest of the PPT

```html
<!DOCTYPE html>
<html lang="en">
<head>
<meta charset="utf-8">
<title>Veltrand Nickel · Data Flow Slide Concepts</title>
<link href="https://fonts.googleapis.com/css2?family=Poppins:wght@400;500;600;700;800&display=swap" rel="stylesheet">
<style>
  :root{
    --page:#eaecef;
    --white:#ffffff;
    --cyan:#1fbfdc;
    --cyan-soft:#5ad2e8;
    --mid:#168fb9;
    --navy:#0b5c83;
    --navy-deep:#084a6c;
    --ink:#1b2430;
    --rule:#c9d0d6;
    --card-bg:#f2f4f6;
    --aqua-bg:#d3f1f7;
    --aqua-line:#a9e3ef;
  }
  *{box-sizing:border-box;margin:0;padding:0}
  html,body{width:1200px;height:2773px;overflow:hidden}
  body{background:var(--page);font-family:'Poppins',sans-serif;color:var(--ink);position:relative}
  .abs{position:absolute}
  .slide{position:absolute;left:50px;width:1100px;height:620px;overflow:hidden}

  .tree{--box-a:var(--cyan);--box-b:var(--navy);--box-stroke:none;--tl:#ffffff;--tv:#ffffff;--line:#8a96a0}
  .tree.on-dark{--box-a:#ffffff;--box-b:#ffffff;--tl:var(--cyan);--tv:var(--navy);--line:#cfe9f2}
  .tree.outline{--box-a:#ffffff;--box-b:#ffffff;--box-stroke:var(--cyan);--tl:var(--cyan);--tv:var(--navy);--line:#8fb8c6}
  .tb-a{fill:var(--box-a);stroke:var(--box-stroke);stroke-width:1.4}
  .tb-b{fill:var(--box-b);stroke:var(--box-stroke);stroke-width:1.4}
  .t-label{fill:var(--tl);font-family:'Poppins',sans-serif;font-size:5.6px;text-anchor:middle}
  .t-value{fill:var(--tv);font-family:'Poppins',sans-serif;font-size:9.5px;font-weight:700;text-anchor:middle}
  .t-line{stroke:var(--line);stroke-width:1;fill:none}

  .icon{stroke:var(--cyan);fill:none;stroke-width:1.6;stroke-linecap:round;stroke-linejoin:round}

  .s1{top:67px;background:var(--white)}
  .col{position:absolute;top:44px;height:531px;background:var(--white);border-radius:14px;box-shadow:0 2px 12px rgba(20,40,60,.12);overflow:hidden}
  .col-head{height:75px;display:flex;align-items:center;justify-content:center;text-align:center;color:#fff;font-weight:800;font-size:19px;line-height:25px;letter-spacing:.2px}
  .head-cyan{background:linear-gradient(180deg,#25c6e0,#16acd0)}
  .head-mid{background:linear-gradient(180deg,#1aa0c8,#1386b2)}
  .head-navy{background:linear-gradient(180deg,#0d6790,#08506f)}
  .src-row{position:absolute;left:18px;width:218px;height:70px;display:flex;align-items:center;gap:14px;font-size:16.5px;font-weight:500}
  .src-row+.src-row{border-top:1px solid var(--rule)}
  .src-row svg{width:36px;height:36px;flex:none}
  .tool{position:absolute;text-align:center;font-size:16.5px;line-height:20px;font-weight:400}
  .tool svg{width:52px;height:52px;display:block;margin:0 auto 8px}
  .chev{position:absolute;width:16px;height:26px}

  .s2{top:740px;background:#f4f5f7;border-bottom:2px solid #d3d7db}
  .s2-inner{position:absolute;left:30px;top:32px;width:1040px;height:556px;background:#f1f2f5;border-radius:20px}
  .pill{position:absolute;top:57px;height:71px;border-radius:36px;color:#fff;font-weight:800;font-size:18.5px;line-height:23px;display:flex;align-items:center;justify-content:center;text-align:center}
  .pill::after{content:"";position:absolute;left:50%;bottom:-10px;margin-left:-10px;border-left:10px solid transparent;border-right:10px solid transparent;border-top:11px solid var(--pc)}
  .card{position:absolute;background:#fff;border-radius:8px;box-shadow:0 1px 6px rgba(20,40,60,.09)}
  .src-card{left:47px;width:218px;height:56px;display:flex;align-items:center;gap:12px;padding-left:12px;font-size:17px;font-weight:500}
  .src-card svg{width:34px;height:34px;flex:none}
  .vrule{position:absolute;width:1px;background:var(--rule)}

  .s3{top:1413px;background:#eef0f2}
  .s4{top:2087px;background:#ffffff}
  .funnel-title{font-family:'Poppins',sans-serif;font-weight:800;font-size:19px;fill:var(--ink)}
  .funnel-list{font-family:'Poppins',sans-serif;font-size:12px;font-weight:500}
  .funnel-tool{font-family:'Poppins',sans-serif;font-size:13.5px;text-anchor:middle}
</style>
</head>
<body>

<svg width="0" height="0" class="abs" aria-hidden="true">
  <defs>
    <linearGradient id="chevGrad" x1="0" y1="0" x2="1" y2="1">
      <stop offset="0" stop-color="#2ac8e2"/><stop offset="1" stop-color="#0f7fae"/>
    </linearGradient>
    <symbol id="chevron" viewBox="0 0 16 26">
      <path d="M0 0H8L16 13L8 26H0L8 13Z" fill="url(#chevGrad)"/>
    </symbol>
    <symbol id="ic-ledger" viewBox="0 0 36 36"><g class="icon"><rect x="6" y="4" width="18" height="28" rx="2"/><path d="M10 10h10M10 15h10M10 20h6"/><rect x="18" y="20" width="12" height="12" rx="1.5"/><path d="M21 24h6M21 28h6"/></g></symbol>
    <symbol id="ic-phone" viewBox="0 0 36 36"><g class="icon"><rect x="11" y="4" width="14" height="28" rx="3"/><circle cx="18" cy="18" r="4"/><path d="M4 14h5M4 22h5M27 14h5M27 22h5"/></g></symbol>
    <symbol id="ic-house" viewBox="0 0 36 36"><g class="icon"><path d="M5 18L16 9L27 18"/><path d="M8 16v14h16V16"/><rect x="13" y="22" width="6" height="8"/><circle cx="27" cy="8" r="4"/></g></symbol>
    <symbol id="ic-gear-hand" viewBox="0 0 36 36"><g class="icon"><circle cx="19" cy="14" r="7"/><circle cx="19" cy="14" r="3"/><path d="M19 4v3M19 21v3M9 14h3M26 14h3"/><path d="M4 27c5-3 9-3 13-1h8c2 0 2 3 0 3h-7"/></g></symbol>
    <symbol id="ic-gears" viewBox="0 0 36 36"><g class="icon"><circle cx="11" cy="14" r="6"/><circle cx="25" cy="14" r="6"/><circle cx="18" cy="9" r="4"/><path d="M4 28h28"/><circle cx="10" cy="28" r="2"/><circle cx="18" cy="28" r="2"/><circle cx="26" cy="28" r="2"/></g></symbol>
    <symbol id="ic-fin" viewBox="0 0 36 36"><g class="icon"><path d="M12 20v-6M17 20V9M22 20v-8M27 20v-4"/><path d="M4 27c5-3 9-3 13-1h8c2 0 2 3 0 3h-7"/></g></symbol>
    <symbol id="ic-tower" viewBox="0 0 52 52"><g class="icon"><rect x="8" y="14" width="20" height="32" rx="1"/><path d="M12 20h4M20 20h4M12 27h4M20 27h4M12 34h4M20 34h4"/><rect x="28" y="26" width="14" height="20"/><circle cx="38" cy="14" r="8"/><path d="M38 10v8M35.5 12h5M35.5 16h5"/><path d="M4 46h44"/></g></symbol>
    <symbol id="ic-chart" viewBox="0 0 52 52"><g class="icon"><path d="M8 44V30M16 44V22M24 44V26M32 44V16"/><path d="M6 22L16 12L24 18L36 6"/><circle cx="38" cy="38" r="8"/><path d="M34.5 38l2.5 2.5 4.5-5"/><path d="M4 46h26"/></g></symbol>
    <symbol id="ic-monitor" viewBox="0 0 52 52"><g class="icon"><rect x="4" y="8" width="44" height="28" rx="2"/><path d="M20 44h12M26 36v8"/><path d="M26 14l8 4v8l-8 4-8-4v-8z"/><path d="M18 18l8 4 8-4M26 22v8"/></g></symbol>
    <symbol id="ic-check" viewBox="0 0 20 20"><circle cx="10" cy="10" r="8.5" fill="none" stroke="currentColor" stroke-width="1.5"/><path d="M6 10.3l2.7 2.7L14 7.6" fill="none" stroke="currentColor" stroke-width="1.6" stroke-linecap="round" stroke-linejoin="round"/></symbol>

    <symbol id="kpi-tree" viewBox="0 0 390 372">
      <g class="t-line">
        <path d="M53 186H68"/>
        <path d="M94 95V281M94 95H136M94 281H136"/>
        <path d="M188 95H202M188 281H202"/>
        <path d="M254 95H262M262 23V120M262 23H272M262 120H272"/>
        <path d="M324 120H330M330 70V164M330 70H337M330 117H337M330 164H337"/>
        <path d="M254 281H262M262 207V305M262 207H272M262 305H272"/>
        <path d="M324 305H330M330 254V348M330 254H337M330 301H337M330 348H337"/>
      </g>
      <g>
        <rect class="tb-a" x="1" y="164" width="52" height="44" rx="4"/><text class="t-label" x="27" y="180">MILL FEED</text><text class="t-value" x="27" y="194">36M</text>
        <rect class="tb-a" x="68" y="164" width="52" height="44" rx="4"/><text class="t-label" x="94" y="180">CRUSHER FEED</text><text class="t-value" x="94" y="194">99.1M</text>
        <rect class="tb-a" x="136" y="73" width="52" height="44" rx="4"/><text class="t-label" x="162" y="89">SURF. TONNES</text><text class="t-value" x="162" y="103">25M</text>
        <rect class="tb-a" x="202" y="73" width="52" height="44" rx="4"/><text class="t-label" x="228" y="89">EQUIP UTIL</text><text class="t-value" x="228" y="103">69.43</text>
        <rect class="tb-a" x="272" y="1" width="52" height="44" rx="4"/><text class="t-label" x="298" y="17">NOH</text><text class="t-value" x="298" y="31">134K</text>
        <rect class="tb-a" x="272" y="98" width="52" height="44" rx="4"/><text class="t-label" x="298" y="114">EQUIP AVAIL (%)</text><text class="t-value" x="298" y="128">85.34</text>
        <rect class="tb-a" x="337" y="48" width="52" height="44" rx="4"/><text class="t-label" x="363" y="64">DELAY</text><text class="t-value" x="363" y="78">46.1K</text>
        <rect class="tb-a" x="337" y="95" width="52" height="44" rx="4"/><text class="t-label" x="363" y="111">DOWN</text><text class="t-value" x="363" y="125">33.1K</text>
        <rect class="tb-a" x="337" y="142" width="52" height="44" rx="4"/><text class="t-label" x="363" y="158">STANDBY</text><text class="t-value" x="363" y="172">46.1K</text>
        <rect class="tb-b" x="136" y="259" width="52" height="44" rx="4"/><text class="t-label" x="162" y="275">UG (TONNES)</text><text class="t-value" x="162" y="289">4.3M</text>
        <rect class="tb-b" x="202" y="259" width="52" height="44" rx="4"/><text class="t-label" x="228" y="275">EQUIP UTIL</text><text class="t-value" x="228" y="289">43.39%</text>
        <rect class="tb-a" x="272" y="185" width="52" height="44" rx="4"/><text class="t-label" x="298" y="201">NOH</text><text class="t-value" x="298" y="215">67K</text>
        <rect class="tb-a" x="272" y="283" width="52" height="44" rx="4"/><text class="t-label" x="298" y="299">EQUIP AVAIL (%)</text><text class="t-value" x="298" y="313">50.98%</text>
        <rect class="tb-b" x="337" y="232" width="52" height="44" rx="4"/><text class="t-label" x="363" y="248">DELAY</text><text class="t-value" x="363" y="262">5.2K</text>
        <rect class="tb-b" x="337" y="279" width="52" height="44" rx="4"/><text class="t-label" x="363" y="295">DOWN</text><text class="t-value" x="363" y="309">22.1K</text>
        <rect class="tb-a" x="337" y="326" width="52" height="44" rx="4"/><text class="t-label" x="363" y="342">STANDBY</text><text class="t-value" x="363" y="356">20.5K</text>
      </g>
    </symbol>

    <symbol id="funnel-titles" viewBox="0 0 1100 620">
      <text class="funnel-title" transform="translate(98 224) rotate(-13)">DATA SOURCES</text>
      <use href="#chevron" x="262" y="166" width="14" height="24"/>
      <text class="funnel-title" transform="translate(316 162) rotate(-12)">DATA MANAGEMENT</text>
      <text class="funnel-title" transform="translate(338 181) rotate(-12)">AND SIMULATION</text>
      <use href="#chevron" x="550" y="101" width="14" height="24"/>
      <text class="funnel-title" transform="translate(623 89) rotate(-12)">VISUALIZATION</text>
      <text class="funnel-title" transform="translate(628 113) rotate(-12)">AND ANALYTICS</text>
    </symbol>
  </defs>
</svg>

<!-- Concept 1: card columns -->
<section class="slide s1">
  <div class="col" style="left:34px;width:253px">
    <div class="col-head head-cyan">DATA SOURCES</div>
    <div style="position:relative">
      <div class="src-row" style="top:5px"><svg><use href="#ic-ledger"/></svg>Ore Accounting</div>
      <div class="src-row" style="top:75px"><svg><use href="#ic-phone"/></svg>Mobile Asset</div>
      <div class="src-row" style="top:146px"><svg><use href="#ic-house"/></svg>Fixed Asset</div>
      <div class="src-row" style="top:217px"><svg><use href="#ic-gear-hand"/></svg>Plant Operations</div>
      <div class="src-row" style="top:288px"><svg><use href="#ic-gears"/></svg>Metals Production</div>
      <div class="src-row" style="top:359px"><svg><use href="#ic-fin"/></svg>Financial</div>
    </div>
  </div>
  <svg class="chev" style="left:296px;top:296px"><use href="#chevron"/></svg>

  <div class="col" style="left:323px;width:293px">
    <div class="col-head head-mid">DATA MANAGEMENT<br>AND SIMULATION</div>
    <div class="vrule" style="left:146px;top:127px;height:204px"></div>
    <div class="tool" style="left:20px;top:170px;width:106px"><svg><use href="#ic-tower"/></svg>Corelink<br>Enterprise</div>
    <svg class="chev" style="left:140px;top:222px;width:12px;height:20px"><use href="#chevron"/></svg>
    <div class="tool" style="left:166px;top:170px;width:106px"><svg><use href="#ic-chart"/></svg>Corelink<br>Analytics</div>
    <div style="position:absolute;left:22px;top:350px;width:250px;height:1px;background:var(--rule)"></div>
    <div style="position:absolute;left:72px;top:380px;display:flex;align-items:center;gap:14px;font-size:16.5px"><svg width="52" height="52"><use href="#ic-monitor"/></svg>Simulation</div>
  </div>
  <svg class="chev" style="left:625px;top:296px"><use href="#chevron"/></svg>

  <div class="col" style="left:652px;width:414px">
    <div class="col-head head-navy">VISUALIZATION<br>AND ANALYTICS</div>
    <svg class="tree abs" style="left:10px;top:108px" width="392" height="374"><use href="#kpi-tree"/></svg>
  </div>
</section>

<!-- Concept 2: pill headers -->
<section class="slide s2">
  <div class="s2-inner">
    <div class="pill head-cyan" style="left:17px;width:218px;--pc:#17b0d2">DATA SOURCES</div>
    <div class="pill head-mid" style="left:308px;width:255px;--pc:#1386b2">DATA MANAGEMENT<br>AND SIMULATION</div>
    <div class="pill head-navy" style="left:636px;width:384px;--pc:#08506f">VISUALIZATION<br>AND ANALYTICS</div>

    <div class="card src-card" style="left:17px;top:121px"><svg><use href="#ic-ledger"/></svg>Ore Accounting</div>
    <div class="card src-card" style="left:17px;top:192px"><svg><use href="#ic-phone"/></svg>Mobile Asset</div>
    <div class="card src-card" style="left:17px;top:263px"><svg><use href="#ic-house"/></svg>Fixed Asset</div>
    <div class="card src-card" style="left:17px;top:334px"><svg><use href="#ic-gear-hand"/></svg>Plant Operations</div>
    <div class="card src-card" style="left:17px;top:405px"><svg><use href="#ic-gears"/></svg>Metals Production</div>
    <div class="card src-card" style="left:17px;top:476px"><svg><use href="#ic-fin"/></svg>Financial</div>

    <div class="vrule" style="left:270px;top:125px;height:408px"></div>
    <svg class="chev" style="left:262px;top:315px"><use href="#chevron"/></svg>

    <div class="card tool" style="left:308px;top:179px;width:110px;height:179px;padding-top:28px"><svg><use href="#ic-tower"/></svg>Corelink<br>Enterprise</div>
    <svg class="chev" style="left:429px;top:258px;width:12px;height:20px"><use href="#chevron"/></svg>
    <div class="card tool" style="left:453px;top:179px;width:110px;height:179px;padding-top:28px"><svg><use href="#ic-chart"/></svg>Corelink<br>Analytics</div>
    <div class="card" style="left:308px;top:375px;width:255px;height:98px;display:flex;align-items:center;justify-content:center;gap:14px;font-size:16.5px"><svg width="52" height="52"><use href="#ic-monitor"/></svg>Simulation</div>

    <div class="vrule" style="left:596px;top:125px;height:408px"></div>
    <svg class="chev" style="left:588px;top:315px"><use href="#chevron"/></svg>

    <div class="card" style="left:628px;top:121px;width:392px;height:412px;border-radius:14px">
      <svg class="tree abs" style="left:10px;top:19px" width="372" height="354"><use href="#kpi-tree"/></svg>
    </div>
  </div>
</section>

<!-- Concept 3: dark funnel -->
<section class="slide s3">
  <svg class="abs" style="left:0;top:0" width="1100" height="620" viewBox="0 0 1100 620">
    <defs>
      <linearGradient id="g3a" x1="0" x2="1"><stop offset="0" stop-color="#27c8e2"/><stop offset="1" stop-color="#16a9cf"/></linearGradient>
      <linearGradient id="g3b" x1="0" x2="1"><stop offset="0" stop-color="#1ba2cb"/><stop offset="1" stop-color="#1283b0"/></linearGradient>
      <linearGradient id="g3c" x1="0" x2="1"><stop offset="0" stop-color="#0f77a4"/><stop offset="1" stop-color="#074a6b"/></linearGradient>
      <linearGradient id="g3cap" x1="0" x2="1"><stop offset="0" stop-color="#ffffff"/><stop offset="1" stop-color="#e6e9ec"/></linearGradient>
    </defs>
    <rect x="30" y="31" width="1040" height="558" rx="20" fill="#ffffff"/>
    <path d="M284 211L125 244Q48 252 48 312Q48 372 125 380L284 418Z" fill="url(#g3a)"/>
    <path d="M499 159L320 200Q257 215 257 312Q257 417 320 430L499 466Z" fill="url(#g3b)" stroke="#fff" stroke-width="10" paint-order="stroke"/>
    <path d="M924 65L515 155Q448 170 448 312Q448 455 515 470L924 563Z" fill="url(#g3c)" stroke="#fff" stroke-width="10" paint-order="stroke"/>
    <ellipse cx="955" cy="314" rx="80" ry="250" fill="url(#g3cap)"/>

    <use href="#funnel-titles" x="0" y="0" width="1100" height="620"/>

    <g class="funnel-list" fill="#fff" style="color:#fff">
      <use href="#ic-check" x="103" y="256" width="13" height="13"/><text x="121" y="267">Ore Accounting</text>
      <use href="#ic-check" x="103" y="275" width="13" height="13"/><text x="121" y="286">Mobile Asset</text>
      <use href="#ic-check" x="103" y="294" width="13" height="13"/><text x="121" y="305">Fixed Asset</text>
      <use href="#ic-check" x="103" y="313" width="13" height="13"/><text x="121" y="324">Plant Operations</text>
      <use href="#ic-check" x="103" y="332" width="13" height="13"/><text x="121" y="343">Metals Production</text>
      <use href="#ic-check" x="103" y="351" width="13" height="13"/><text x="121" y="362">Financial</text>
    </g>
    <g fill="#fff" style="color:#fff">
      <use href="#ic-check" x="296" y="258" width="20" height="20"/>
      <text class="funnel-tool" x="307" y="295">Corelink</text><text class="funnel-tool" x="307" y="311">Enterprise</text>
      <use href="#chevron" x="349" y="264" width="10" height="18"/>
      <use href="#ic-check" x="391" y="258" width="20" height="20"/>
      <text class="funnel-tool" x="402" y="295">Corelink</text><text class="funnel-tool" x="402" y="311">Analytics</text>
      <path d="M275 337H438" stroke="#bfe6f2" stroke-width="1"/>
      <use href="#ic-check" x="324" y="355" width="20" height="20"/>
      <text class="funnel-tool" x="380" y="370">Simulation</text>
    </g>
    <svg class="tree on-dark" x="477" y="127" width="375" height="358"><use href="#kpi-tree"/></svg>
  </svg>
</section>

<!-- Concept 4: light funnel -->
<section class="slide s4">
  <svg class="abs" style="left:0;top:0" width="1100" height="620" viewBox="0 0 1100 620">
    <defs>
      <linearGradient id="g4cap" x1="0" x2="1"><stop offset="0" stop-color="#bff0f8"/><stop offset="1" stop-color="#67d3e8"/></linearGradient>
    </defs>
    <rect x="30" y="31" width="1040" height="558" rx="20" fill="var(--aqua-bg)"/>
    <path d="M284 211L125 244Q48 252 48 312Q48 372 125 380L284 418Z" fill="#ffffff"/>
    <path d="M499 159L320 200Q257 215 257 312Q257 417 320 430L499 466Z" fill="#ffffff" stroke="#d3f1f7" stroke-width="10" paint-order="stroke"/>
    <path d="M260 330Q261 235 305 210" fill="none" stroke="#a9e3ef" stroke-width="8" stroke-linecap="round"/>
    <path d="M924 65L515 155Q448 170 448 312Q448 455 515 470L924 563Z" fill="#ffffff" stroke="#d3f1f7" stroke-width="10" paint-order="stroke"/>
    <path d="M451 330Q452 205 495 172" fill="none" stroke="#a9e3ef" stroke-width="8" stroke-linecap="round"/>
    <ellipse cx="955" cy="314" rx="80" ry="250" fill="url(#g4cap)"/>

    <use href="#funnel-titles" x="0" y="0" width="1100" height="620"/>

    <g class="funnel-list" fill="#1b2430" style="color:#1fbfdc">
      <use href="#ic-check" x="103" y="256" width="13" height="13"/><text x="121" y="267">Ore Accounting</text>
      <use href="#ic-check" x="103" y="275" width="13" height="13"/><text x="121" y="286">Mobile Asset</text>
      <use href="#ic-check" x="103" y="294" width="13" height="13"/><text x="121" y="305">Fixed Asset</text>
      <use href="#ic-check" x="103" y="313" width="13" height="13"/><text x="121" y="324">Plant Operations</text>
      <use href="#ic-check" x="103" y="332" width="13" height="13"/><text x="121" y="343">Metals Production</text>
      <use href="#ic-check" x="103" y="351" width="13" height="13"/><text x="121" y="362">Financial</text>
    </g>
    <g fill="#1b2430" style="color:#1fbfdc">
      <use href="#ic-check" x="296" y="258" width="20" height="20"/>
      <text class="funnel-tool" x="307" y="295">Corelink</text><text class="funnel-tool" x="307" y="311">Enterprise</text>
      <use href="#chevron" x="351" y="266" width="8" height="14"/>
      <use href="#ic-check" x="391" y="258" width="20" height="20"/>
      <text class="funnel-tool" x="402" y="295">Corelink</text><text class="funnel-tool" x="402" y="311">Analytics</text>
      <use href="#ic-check" x="324" y="355" width="20" height="20"/>
      <text class="funnel-tool" x="380" y="370">Simulation</text>
    </g>
    <svg class="tree outline" x="477" y="127" width="375" height="358"><use href="#kpi-tree"/></svg>
  </svg>
</section>

</body>
</html>
```